Flyer für Personalreferentin
Zielgruppe
Freiberufliche Personalreferentin. Ich unterstütze Unternehmen (zeitweise) in den Personalabteilungen (Rekrutierung, Personalverwaltung, Mitarbeiterbetreuung). Zielgruppe sind Unternehmen, die moderne Personalarbeit abbilden möchten.
Aufgabenstellung
Der Flyer soll 2-seitig sein. Seite 1 - Werbetext und Seite 2 bzw. Rückseite mein Profil bzw. meinen Lebenslauf ansprechend dargestellt. Ich möchte ein modernes, minimalistisches Design.
Ziel wäre einen Flyer zu erhalten, den man an die Unternehmen senden kann um auf die Dienstleistung aufmerksam zu machen. Logo und Profilbild sollen verwendet werden, weitere Bilder gern mitvorschlagen.

```html
<!DOCTYPE html>
<html lang="de">
<head>
<meta charset="utf-8">
<title>Flyer Personalreferentin – Monika Lüers</title>
<link rel="stylesheet" href="https://fonts.googleapis.com/css2?family=Poppins:ital,wght@0,300;0,400;0,600;0,700;0,800;1,400&family=Source+Sans+3:ital,wght@0,400;0,600;0,700;1,400&display=swap">
<style>
:root{
  --red:#c94a36;
  --grey:#58585a;
  --ink:#1d1d1d;
  --text:#333;
  --paper:#fff;
  --stage:#ececec;
  --photo-a:#e9e6e2;
  --photo-b:#b89a7c;
}
*{box-sizing:border-box;margin:0;padding:0}
html,body{width:909px;height:1200px;overflow:hidden;background:var(--stage)}
body{position:relative;font-family:"Source Sans 3",Arial,sans-serif;color:var(--text)}
.spread{position:absolute;left:34px;width:840px;height:570px;display:flex;background:var(--paper);box-shadow:0 6px 18px rgba(0,0,0,.12)}
.spread--outside{top:20px}
.spread--inside{top:610px}
.panel{position:relative;width:280px;height:100%;overflow:hidden}
.panel + .panel{border-left:1px solid #e6e6e6}

/* Outside – cover */
.brand{position:absolute;top:34px;left:0;width:100%;text-align:center}
.brand__name{font-family:"Poppins",sans-serif;font-weight:300;font-size:26px;color:var(--grey);display:inline-flex;align-items:center;gap:8px}
.brand__dot{width:10px;height:10px;border-radius:50%;background:var(--red)}
.brand__role{font-family:"Poppins",sans-serif;font-size:10px;color:var(--grey);margin-top:2px}
.photo{position:absolute;background:linear-gradient(160deg,var(--photo-a) 0%,#d8d2cb 45%,var(--photo-b) 100%)}
.cover .photo{left:0;top:110px;width:280px;height:300px}
.cover__band{position:absolute;left:0;top:400px;width:280px;height:170px;background:var(--red);padding:26px 22px}
.cover__claim{font-family:"Poppins",sans-serif;font-weight:600;font-size:12.5px;line-height:1.45;color:#fff;text-transform:uppercase}
.bar-grey{position:absolute;bottom:0;height:16px;background:var(--grey)}

/* Outside – intro */
.intro{padding:40px 22px 0}
.intro__title{font-family:"Poppins",sans-serif;font-weight:700;font-size:17px;color:var(--ink);margin-bottom:10px}
.accent{color:var(--red)}
.copy{font-size:8.4px;line-height:1.5}
.lead-red{font-family:"Poppins",sans-serif;font-weight:600;font-size:8.6px;color:var(--red);margin:16px 0 14px}
.benefit{display:flex;gap:12px;margin-bottom:18px}
.benefit__icon{flex:0 0 42px;height:42px}
.benefit__icon svg{width:42px;height:42px;fill:none;stroke:var(--red);stroke-width:1.6;stroke-linecap:round;stroke-linejoin:round}
.benefit__title{font-family:"Poppins",sans-serif;font-weight:600;font-size:8.8px;color:var(--red);margin-bottom:3px}

/* Outside – contact */
.contact-panel{padding:36px 22px 0}
.contact-panel .photo{left:0;top:262px;width:280px;height:120px;background:linear-gradient(120deg,#d9d3cb,#9a8a79 60%,#5c5450)}
.contact-box{position:absolute;left:0;top:382px;width:280px;height:172px;background:var(--red);color:#fff;padding:22px 22px}
.contact-box .copy{color:#fff;font-size:9px}
.contact-grid{display:flex;justify-content:space-between;margin-top:22px;font-size:8.6px;line-height:1.55}
.contact-line{display:flex;align-items:flex-start;gap:5px}
.contact-line svg{width:9px;height:9px;margin-top:2px;fill:#fff;flex:none}

/* Inside – profile */
.profile__name{position:absolute;left:26px;top:34px;font-family:"Poppins",sans-serif;font-weight:800;font-size:30px;line-height:.98;color:var(--ink);text-transform:uppercase}
.profile__role{position:absolute;left:26px;top:100px;font-family:"Poppins",sans-serif;font-size:12px;color:var(--ink)}
.profile .photo{left:0;top:128px;width:280px;height:300px}
.profile__box{position:absolute;left:0;top:410px;width:280px;height:140px;background:var(--red);border-top-right-radius:40px;color:#fff;padding:20px 22px;font-size:9.4px;line-height:1.55}
.profile__box b{font-weight:700}
.profile__contacts{display:flex;justify-content:space-between;margin-top:8px}

/* Inside – CV */
.quote{position:absolute;left:314px;top:24px;width:510px;display:flex;gap:10px;font-size:8.6px;font-style:italic;line-height:1.5;z-index:2}
.quote__mark{font-family:"Poppins",sans-serif;font-weight:700;font-size:34px;line-height:.8;color:var(--red)}
.cv{padding:84px 22px 0}
.section-title{font-family:"Poppins",sans-serif;font-weight:700;font-size:14px;color:var(--ink);margin-bottom:8px}
.job{margin-bottom:10px;font-size:8.2px;line-height:1.42}
.job__title{font-weight:700;color:var(--ink)}
.job__org{color:var(--red);font-style:italic}
.job__date{font-style:italic}
.job ul{padding-left:11px;margin-top:2px}
.divider{position:absolute;left:0;top:96px;width:280px;height:12px}
.cv--right{padding-top:128px}
.skills{position:absolute;left:0;top:400px;width:280px;height:150px;background:var(--red);border-top-left-radius:36px;color:#fff;padding:24px 24px}
.skills__title{font-family:"Poppins",sans-serif;font-weight:600;font-size:10.5px;margin-bottom:16px;text-align:center}
.skill{display:flex;align-items:center;gap:12px;font-size:9px}
.skill__label{width:50px}
.skill__bars{display:flex;gap:5px}
.skill__bars span{width:26px;height:3px;background:#fff}
.skill__bars span.off{background:#a63a29}
.skill__level{text-align:right;font-style:italic;font-size:8.6px;margin:4px 0 12px}
</style>
</head>
<body>

<section class="spread spread--outside">
  <div class="panel cover">
    <div class="brand">
      <div class="brand__name"><span class="brand__dot"></span>monika lüers</div>
      <div class="brand__role">HR Freelancer</div>
    </div>
    <div class="photo" role="img" aria-label="Porträtfoto der Personalreferentin mit verschränkten Armen im Büro"></div>
    <div class="cover__band">
      <p class="cover__claim">Sie suchen einen erfahrenen Personalreferenten mit einem modernen Verständ­nis von Personalarbeit und Mitarbeiterführung?</p>
    </div>
    <div class="bar-grey" style="left:0;width:170px"></div>
  </div>

  <div class="panel intro">
    <h2 class="intro__title">Hallo, Ich bin Monika <span class="accent">Lüers</span></h2>
    <p class="copy">Ich biete Ihnen 10 Jahre Berufserfahrung, nachgewiesene Expertise in der Personalentwicklung und Führung, sowie eine empathische, diskrete und zuverlässige Arbeitsweise. Als freiberuflicher Personalreferent stehe ich Ihnen flexibel und bedarfsgerecht zur Verfügung, um Ihr Unternehmen erfolgreich zu unterstützen.</p>
    <p class="lead-red">Ein freiberuflicher Personalreferent bietet zudem eine Reihe von Vorteilen:</p>
    <div class="benefit">
      <div class="benefit__icon"><svg viewBox="0 0 42 42"><path d="M21 38V22M21 22L9 12M21 22l12-10M21 22V6M6 15l3-3 3 1M30 13l3-1 1 3M18 9l3-3 3 3"/></svg></div>
      <div><p class="benefit__title">Flexibilität</p><p class="copy">Als Freiberufler können Personalreferenten flexibel auf die Anforderungen und Bedürfnisse eines Unternehmens reagieren. Sie können sowohl für kurzfristige Projekte als auch für langfristige Engagements engagiert werden, je nach Bedarf des Unternehmens.</p></div>
    </div>
    <div class="benefit">
      <div class="benefit__icon"><svg viewBox="0 0 42 42"><circle cx="21" cy="11" r="7"/><path d="M9 31c0-7 5-11 12-11s12 4 12 11"/><path d="M8 38l2-4 2 4M19 38l2-4 2 4M30 38l2-4 2 4"/></svg></div>
      <div><p class="benefit__title">Fachkenntnisse und Erfahrung</p><p class="copy">Freiberufliche Personalreferenten verfügen in der Regel über umfangreiche Fachkenntnisse und langjährige Erfahrung in verschiedenen Branchen. Sie bringen wertvolles Know-how und Best Practices mit, um effektive HR-Strategien und -Prozesse zu entwickeln und umzusetzen.</p></div>
    </div>
    <div class="benefit">
      <div class="benefit__icon"><svg viewBox="0 0 42 42"><circle cx="21" cy="14" r="8"/><path d="M24 10h-4a3 3 0 000 8h4M17 13h6M17 15h6"/><path d="M4 30h8l6 3h10l8-5v4l-9 6H14l-10-3z"/><path d="M7 6v8M5 12l2 2 2-2M35 6v8M33 12l2 2 2-2"/></svg></div>
      <div><p class="benefit__title">Kostenersparnis</p><p class="copy">Die Beauftragung eines freiberuflichen Personalreferenten kann kostengünstiger sein als die Einstellung eines festangestellten Mitarbeiters. Unternehmen können die Kosten für Sozialleistungen, Lohnnebenkosten und Fortbildungsmaßnahmen einsparen.</p></div>
    </div>
  </div>

  <div class="panel contact-panel">
    <div class="benefit">
      <div class="benefit__icon"><svg viewBox="0 0 42 42"><circle cx="19" cy="11" r="7"/><path d="M6 36c0-8 6-13 13-13"/><circle cx="31" cy="29" r="6"/><path d="M28 35l-1 5 4-2 4 2-1-5"/></svg></div>
      <div><p class="benefit__title">Spezialisierung</p><p class="copy">Freiberufliche Personalreferenten können auf bestimmte HR-Bereiche spezialisiert sein, wie z.B. Rekrutierung, Personalentwicklung oder Arbeitsrecht. Unternehmen können von dieser Spezialisierung profitieren und sich auf Expertenwissen verlassen, um spezifische HR-Herausforderungen anzugehen.</p></div>
    </div>
    <div class="benefit">
      <div class="benefit__icon"><svg viewBox="0 0 42 42"><rect x="4" y="12" width="34" height="24" rx="3"/><path d="M15 12V8h12v4M4 22h34M19 22v3h4v-3"/></svg></div>
      <div><p class="benefit__title">Unabhängigkeit</p><p class="copy">Freiberufliche Personalreferenten arbeiten selbstständig und eigenverantwortlich. Sie bringen frische Perspektiven und neue Ideen in das Unternehmen ein, ohne von internen Strukturen oder Unternehmenskulturen beeinflusst zu sein.</p></div>
    </div>
    <div class="photo" role="img" aria-label="Foto eines Händedrucks zweier Geschäftsleute"></div>
    <div class="contact-box">
      <p class="copy">Kontaktieren Sie mich jetzt, um zu erfahren, wie ich Ihre HR-Prozesse optimieren und Ihr Team zum Erfolg führen kann.</p>
      <div class="contact-grid">
        <div class="contact-line"><svg viewBox="0 0 10 10"><path d="M5 0a3.5 3.5 0 013.5 3.5C8.5 6 5 10 5 10S1.5 6 1.5 3.5A3.5 3.5 0 015 0zm0 2a1.5 1.5 0 100 3 1.5 1.5 0 000-3z"/></svg><span>Lindenweg 14<br>D-14482 Waldenau</span></div>
        <div>
          <div class="contact-line"><svg viewBox="0 0 10 10"><path d="M2 0l2 2-1 1.5a6 6 0 003.5 3.5L8 6l2 2-1.5 2C4 10 0 6 0 1.5z"/></svg><span>0176 48 19 05 27</span></div>
          <div class="contact-line"><svg viewBox="0 0 10 10"><path d="M0 2h10v6H0zM0 2l5 3.5L10 2"/></svg><span>mail@monikaluers.de</span></div>
        </div>
      </div>
    </div>
    <div class="bar-grey" style="right:0;width:150px"></div>
  </div>
</section>

<section class="spread spread--inside">
  <div class="panel profile">
    <h1 class="profile__name">Monika<br><span class="accent">Lüers</span></h1>
    <p class="profile__role">Freelance Personalbereich</p>
    <div class="photo" role="img" aria-label="Porträtfoto der Personalreferentin mit verschränkten Armen im Büro"></div>
    <div class="profile__box">
      <p><b>Geburtsdatum/ -ort:</b> 14.06.1988 in Elbhagen</p>
      <div class="profile__contacts">
        <div class="contact-line"><svg viewBox="0 0 10 10" style="width:9px;height:9px;fill:#fff"><path d="M5 0a3.5 3.5 0 013.5 3.5C8.5 6 5 10 5 10S1.5 6 1.5 3.5A3.5 3.5 0 015 0zm0 2a1.5 1.5 0 100 3 1.5 1.5 0 000-3z"/></svg><span>Lindenweg 14<br>D-14482 Waldenau</span></div>
        <div>
          <div class="contact-line"><svg viewBox="0 0 10 10" style="width:9px;height:9px;fill:#fff"><path d="M2 0l2 2-1 1.5a6 6 0 003.5 3.5L8 6l2 2-1.5 2C4 10 0 6 0 1.5z"/></svg><span>0176 48 19 05 27</span></div>
          <div class="contact-line"><svg viewBox="0 0 10 10" style="width:9px;height:9px;fill:#fff"><path d="M0 2h10v6H0zM0 2l5 3.5L10 2"/></svg><span>mail@monikaluers.de</span></div>
        </div>
      </div>
    </div>
  </div>

  <div class="quote">
    <span class="quote__mark">“</span>
    <p>Für die Tätigkeit im Personalwesen bringe ich ein abgeschlossenes Studium im Personalbereich, aufgrund meiner Ausbildung zur Hotelfachfrau den notwendigen Dienstleistungsgedanken sowie umfassende praktische Erfahrungen in verschiedenen Bereichen der Personalarbeit.</p>
  </div>

  <div class="panel cv">
    <h2 class="section-title">Berufliche <span class="accent">Erfahrung</span></h2>
    <div class="job">
      <p class="job__title">HR Generalist</p>
      <p class="job__org">Nordlicht Service GmbH, Berlin</p>
      <p class="job__date">03.2018 – 12.2023</p>
      <ul><li>Personalbetreuung und -verwaltung</li><li>vorbereitende Lohn- und Gehaltsabrechnung</li><li>Durchführung des BEM-Verfahrens</li><li>Rekrutierung</li></ul>
    </div>
    <div class="job">
      <p class="job__title">HR Assistant Manager / Recruitment Manager</p>
      <p class="job__org">Fasana Mode Ltd. &amp; Co. KG, Berlin und deutschlandweit</p>
      <p class="job__date">09.2014 – 02.2018</p>
      <ul><li>Personalbetreuung und -verwaltung</li><li>Deutschlandweite Rekrutierung von Mitarbeitern u.a. im Rahmen von Filialeröffnungen</li><li>Durchführen von Bewerbungsinterviews an Standorten bundesweit</li><li>Begleitung des kompletten Einstellungsprozesses</li><li>Unterstützung des Führungsteams</li><li>Kontrolle der Gehaltsabrechnung und des Berichtswesens</li><li>Zusammenarbeit mit der Arbeitnehmervertretung</li></ul>
    </div>
    <h2 class="section-title" style="margin-top:12px">Berufsaus- <span class="accent">und Weiterbildung</span></h2>
    <div class="job">
      <p class="job__title">Studium der Betriebswirtschaftslehre</p>
      <p><span class="job__org">HWS Berlin</span> <span class="job__date">10.2008 – 03.2012</span></p>
      <ul><li>Abschluss: Bachelor of Arts (B.A.)</li><li>Schwerpunkt Personal und Organisation</li></ul>
    </div>
    <div class="job">
      <p class="job__title">Ausbildung zur Hotelfachfrau</p>
      <p><span class="job__org">Elbufer Hotel Elbhagen</span> <span class="job__date">08.2006 – 07.2008</span></p>
    </div>
  </div>

  <div class="panel cv cv--right">
    <svg class="divider" viewBox="0 0 280 12" preserveAspectRatio="none"><path d="M0 2h30l20 9h230" fill="none" stroke="var(--red)" stroke-width="1.5"/></svg>
    <div class="job">
      <p class="job__title">HR Coordinator</p>
      <p class="job__org">Havelhof Hotel Gruppe, Berlin</p>
      <p class="job__date">08.2013 – 08.2014</p>
      <ul><li>Operative Personalarbeit von Recruiting inkl. Stellenausschreibungen, über Vertragsgestaltung, zu Personalbetreuung bis zur Abwicklung aller Formalitäten bei Austritten</li><li>Implementierung und Weiterentwicklung bestehender HR-Prozesse</li><li>Personalverwaltung einzelner Häuser europaweit, inkl. vorbereitende Lohn- und Gehaltsabrechnung</li><li>Präsentation des Unternehmens auf Messen, Schulen etc.</li><li>Mitarbeit an verschiedenen HR-Projekten wie z.B. Einführung eines unternehmensweiten Sprachkurses</li></ul>
    </div>
    <div class="job">
      <p class="job__title">Praktikum in der Personalabteilung</p>
      <p class="job__org">Alpenblick Hotel Berlin, Alpenblick Hotels &amp; Resorts, Berlin</p>
      <p class="job__date">09.2010 – 02.2011</p>
      <ul><li>Vorbereitung und Abwicklung aller Formalitäten bei der Einstellung neuer Mitarbeiter</li><li>Pflegen der Online-Recruitingportale</li><li>Gestaltung von Stellenanzeigen</li></ul>
    </div>
    <div class="skills">
      <p class="skills__title">BERUFSAUS- UND WEITERBILDUNG</p>
      <div class="skill"><span class="skill__label">Englisch</span><span class="skill__bars"><span></span><span></span><span></span><span></span><span></span></span></div>
      <p class="skill__level">verhandlungssicher</p>
      <div class="skill"><span class="skill__label">Spanisch</span><span class="skill__bars"><span></span><span></span><span class="off"></span><span class="off"></span><span class="off"></span></span></div>
      <p class="skill__level">Grundkenntnisse</p>
    </div>
  </div>
</section>

</body>
</html>
```